Label for kLw Homestead beef tallow

I need a small label to go on a 2oz amber glass jar as well as a 4 oz. amber glass jar of moisturizer.
I prefer it to be rectangular for the 2oz jar since it's small and square for the 4oz jar.
I'd like to keep our kLw Homestead logo the same font and style, which is attached. Ten Sleep, Wyoming should be left out. The font for kLw Homestead is spartan.
The label content is as follows:
Heritage Tallow
Whipped Moisturizer
Ingredients: Beef Tallow, jojoba oil, peppermint oil.
2oz. jar

Instead of a white label, I'm thinking of a tan or brown label that will blend in with the amber jar. The lettering could then be a white, cream or even rust/burgandy color. Something to give it a rich look.

Thank you!

Target Market(s)

Mainly women but men as well.

Industry/Entity Type

Ranching and online beef sales

Requirements
Must have
• kLw Homestead logo

```html
<!DOCTYPE html>
<html lang="en">
<head>
<meta charset="utf-8">
<title>kLw Homestead – Heritage Tallow Label</title>
<link rel="stylesheet" href="https://fonts.googleapis.com/css2?family=Fira+Sans+Condensed:wght@700&family=PT+Sans:wght@400;700&display=swap">
<style>
  :root {
    --backdrop: #5c4033;
    --label-tan: #dcc197;
    --label-tan-deep: #cfb07f;
    --rust-red: #a71d26;
    --ink-red: #8c1820;
    --cream: #ecd9b8;
  }
  * { margin: 0; padding: 0; box-sizing: border-box; }
  html, body {
    width: 1200px;
    height: 643px;
    overflow: hidden;
    background: var(--backdrop);
  }
  .canvas {
    width: 1200px;
    height: 643px;
    display: flex;
    align-items: center;
    justify-content: center;
  }
  .jar-label {
    width: 560px;
    height: 560px;
    display: block;
    filter: drop-shadow(0 10px 14px rgba(0, 0, 0, 0.35));
  }
  .label-sheet { fill: var(--label-tan); }
  .label-frame,
  .badge-outline,
  .subtitle-ribbon {
    fill: none;
    stroke: var(--rust-red);
    stroke-linejoin: round;
  }
  .label-frame { stroke-width: 7; }
  .badge-outline { stroke-width: 10; }
  .subtitle-ribbon { stroke-width: 5; }
  .logo-seal { fill: var(--rust-red); }
  .logo-seal-ring { fill: none; stroke: var(--ink-red); stroke-width: 4; }
  .logo-name {
    font-family: "PT Sans", sans-serif;
    font-weight: 400;
    fill: var(--cream);
  }
  .flourish { fill: var(--rust-red); }
  .product-title {
    font-family: "Fira Sans Condensed", sans-serif;
    font-weight: 700;
    font-size: 66px;
    fill: var(--rust-red);
    letter-spacing: 1px;
  }
  .product-subtitle {
    font-family: "PT Sans", sans-serif;
    font-weight: 700;
    font-size: 33px;
    fill: var(--ink-red);
  }
  .jar-size,
  .ingredients-heading,
  .ingredients-list {
    font-family: "PT Sans", sans-serif;
    font-weight: 400;
    fill: var(--ink-red);
  }
  .jar-size { font-size: 42px; letter-spacing: 1px; }
  .ingredients-heading { font-size: 33px; }
  .ingredients-list { font-size: 36px; }
  .ingredients-rule { stroke: var(--rust-red); stroke-width: 2.5; }
</style>
</head>
<body>
<main class="canvas">
  <svg class="jar-label" viewBox="0 0 876 876" xmlns="http://www.w3.org/2000/svg" aria-label="Heritage Tallow whipped moisturizer jar label">
    <rect class="label-sheet" x="0" y="0" width="876" height="876"/>

    <path class="label-frame" d="M 52 32 L 824 32 A 30 30 0 0 0 854 62 L 854 814 A 30 30 0 0 0 824 844 L 52 844 A 30 30 0 0 0 22 814 L 22 62 A 30 30 0 0 0 52 32 Z"/>

    <path class="badge-outline" d="M 320 212 L 100 300 Q 70 312 72 345 L 110 500 Q 116 518 140 528 L 420 645 Q 438 652 456 645 L 736 528 Q 760 518 766 500 L 804 345 Q 806 312 776 300 L 556 212"/>

    <path class="subtitle-ribbon" d="M 150 483 L 726 483 L 650 540 L 226 540 Z"/>

    <rect class="flourish" x="150" y="296" width="150" height="60" rx="28" role="img" aria-label="Curled scroll ornament, left"/>
    <rect class="flourish" x="576" y="296" width="150" height="60" rx="28" role="img" aria-label="Curled scroll ornament, right"/>
    <rect class="flourish" x="336" y="548" width="60" height="60" rx="22" role="img" aria-label="Small hooked scroll ornament, left"/>
    <rect class="flourish" x="480" y="548" width="60" height="60" rx="22" role="img" aria-label="Small hooked scroll ornament, right"/>

    <circle class="logo-seal" cx="438" cy="238" r="136"/>
    <circle class="logo-seal-ring" cx="438" cy="238" r="122"/>
    <text class="logo-name" x="438" y="258" text-anchor="middle" font-size="80">kLw</text>
    <text class="logo-name" x="438" y="310" text-anchor="middle" font-size="32" letter-spacing="2">Homestead</text>

    <text class="product-title" x="438" y="455" text-anchor="middle">HERITAGE TALLOW</text>
    <text class="product-subtitle" x="438" y="522" text-anchor="middle">WHIPPED MOISTURIZER</text>

    <text class="jar-size" x="792" y="668" text-anchor="end">2oz.jar</text>

    <text class="ingredients-heading" x="437" y="727" text-anchor="middle">Ingredients</text>
    <line class="ingredients-rule" x1="260" y1="748" x2="615" y2="748"/>
    <text class="ingredients-list" x="437" y="796" text-anchor="middle">Beef tallow, jojoba oil, peppermint oil</text>
  </svg>
</main>
</body>
</html>
```